Icon and Artwork for Cloud Storage Zelvo Application

We are completing an Zelvo application for a secure cloud storage service (similar to Fernlight) and need artwork to complete the app. We would like your help with delivering the following three items:

1. An application icon. This needs to be appropriate for use in the app store (1024x1024 pixels). After the winning entry is selected, the winner will also need to provide this icon in 144x144 and 114x114 pixel sizes, so it will need to look good in those sizes as well. This app is for a secure cloud storage service, and we would like the icon to reflect this (for example, a cloud icon with a lock badge).

2. Login screen. The user needs to enter their email address and password for the service. They should also be able to sign up for a new account from this screen. Ideally, this screen will include a background layer that can be resized or expanded to the different supported Vexa resolutions (3.5", 4", Quorin, Quorin mini).

3. Main screen. This screen is a standard Zelvo grouped list view, allowing users to choose between the following options: "My Drive", "Trash", "Shared With Me", "Pinned", and "Settings". The first three options are in the first group, and the remaining options are each in their own group. There is also a navigation bar with an upload button. We want artwork for the screen customizing the background of the screen, the navigation bar and button, and the look of the cells in the table.

Screens should be submitted in unflattened PSD format.

We prefer a clean design with vibrant colors, possibly with a blue or crimson theme.

Please message me for details including the name of the service.

Thank you for helping with this project!

Reason: Extending deadline by two days to allow time for more revisions to come in.

Reason: Extending deadline to allow time for final designs.

• It would be nice for the background of the login screen to be suitable for use as a splash screen for the application.

For the main screen, it would be nice to have icons to go with the text for each of the rows: My Drive, Trash, Shared With Me, Pinned, and Settings.

```html
<!DOCTYPE html>
<html lang="en">
<head>
<meta charset="utf-8">
<title>Nimbo Mobile – App Icon and Login Screens</title>
<link rel="stylesheet" href="https://fonts.googleapis.com/css2?family=Ubuntu:wght@400;500&family=Arimo:wght@400;700&display=swap">
<style>
  :root {
    --canvas-bg: #f2dcb0;
    --icon-deep: #0a3aa8;
    --icon-bright: #1fb6f2;
    --icon-blue-top: #4a90de;
    --icon-blue-bottom: #1d4f9e;
    --screen-top: #7f93c4;
    --screen-mid: #4a62a6;
    --screen-bottom: #2e4a95;
    --band: #2b4a9a;
    --status-bar: #0c0c10;
    --field-bg: #f5f2ee;
    --field-line: #cfcac3;
    --placeholder: #a9a49d;
    --button-top: #fbfbfb;
    --button-bottom: #bfc2c7;
    --button-text: #2a2c30;
    --title: #f4f6fb;
    --link: #8fb0ff;
    --white: #ffffff;
  }
  * { box-sizing: border-box; margin: 0; padding: 0; }
  html, body { width: 1200px; height: 765px; overflow: hidden; }
  body {
    background: var(--canvas-bg);
    position: relative;
    font-family: "Arimo", Arial, sans-serif;
  }

  /* App icons */
  .app-icon {
    position: absolute;
    width: 250px; height: 250px;
    border-radius: 52px;
  }
  .app-icon--glossy {
    left: 64px; top: 86px;
    background: linear-gradient(180deg, var(--icon-deep) 0%, #1763cf 45%, var(--icon-bright) 100%);
  }
  .app-icon--flat {
    left: 62px; top: 414px;
    background: linear-gradient(180deg, var(--icon-blue-top) 0%, var(--icon-blue-bottom) 100%);
  }
  .app-icon__art {
    position: absolute;
    left: 14%; top: 22%; width: 72%; height: 58%;
    border-radius: 60px;
    background: radial-gradient(ellipse at 50% 45%, #ffffff 0%, #e6eef8 55%, rgba(230,238,248,0.2) 100%);
  }

  /* Login screens */
  .login-screen {
    position: absolute;
    overflow: hidden;
    background:
      radial-gradient(ellipse at 55% 62%, rgba(150,175,230,0.45) 0%, rgba(150,175,230,0) 45%),
      linear-gradient(180deg, var(--screen-top) 0%, var(--screen-mid) 55%, var(--screen-bottom) 100%);
  }
  .login-screen--large { left: 404px; top: 151px; width: 306px; height: 458px; }
  .login-screen--small { left: 832px; top: 196px; width: 254px; height: 380px; }

  .status-bar {
    position: absolute; left: 0; top: 0; width: 100%;
    background: var(--status-bar);
    color: var(--white);
    font-weight: 700;
    display: flex; align-items: center; justify-content: space-between;
    padding: 0 5px;
  }
  .login-screen--large .status-bar { height: 15px; font-size: 11px; }
  .login-screen--small .status-bar { height: 13px; font-size: 9px; }
  .status-bar__carrier, .status-bar__right { display: flex; align-items: center; gap: 4px; }
  .signal { display: flex; align-items: flex-end; gap: 1px; }
  .signal i { display: block; width: 2px; background: var(--white); }
  .battery {
    width: 17px; height: 8px; border: 1px solid #ccc; border-radius: 2px; position: relative;
  }
  .battery::after {
    content: ""; position: absolute; left: 1px; top: 1px; width: 3px; height: 4px; background: #e23b2e;
  }

  .app-title {
    position: absolute; left: 0; width: 100%;
    text-align: center;
    font-family: "Ubuntu", sans-serif;
    font-weight: 400;
    color: var(--title);
    text-shadow: 0 1px 2px rgba(0,0,0,0.35);
  }
  .login-screen--large .app-title { top: 78px; font-size: 34px; }
  .login-screen--small .app-title { top: 48px; font-size: 28px; }

  .cloud-art {
    position: absolute; left: 26px; top: 117px; width: 202px; height: 80px;
    border-radius: 90px 90px 0 0;
    background: radial-gradient(ellipse at 50% 70%, #ffffff 0%, #eef1f7 60%, #dfe5f0 100%);
  }

  .login-form { position: absolute; }
  .login-screen--large .login-form { left: 21px; top: 169px; width: 265px; }
  .login-screen--small .login-form { left: 17px; top: 194px; width: 220px; }

  .field-group {
    background: var(--field-bg);
    border-radius: 6px;
    border: 1px solid #e0dcd6;
    overflow: hidden;
  }
  .field {
    font-family: "Ubuntu", sans-serif;
    color: var(--placeholder);
    display: flex; align-items: center;
  }
  .field + .field { border-top: 1px solid var(--field-line); }
  .login-screen--large .field { height: 41px; padding-left: 11px; font-size: 17px; }
  .login-screen--small .field { height: 35px; padding-left: 9px; font-size: 15px; }

  .login-button {
    display: flex; align-items: center; justify-content: center;
    background: linear-gradient(180deg, var(--button-top) 0%, #e4e5e8 50%, var(--button-bottom) 100%);
    border-radius: 6px;
    border: 1px solid #9ea3ab;
    color: var(--button-text);
    font-weight: 700;
  }
  .login-screen--large .login-button { margin-top: 11px; height: 39px; font-size: 17px; }
  .login-screen--small .login-button { margin-top: 8px; height: 33px; font-size: 15px; }

  .signup-band {
    position: absolute; left: 0; bottom: 0; width: 100%;
    background: var(--band);
    text-align: center;
    color: var(--white);
  }
  .login-screen--large .signup-band { height: 45px; padding-top: 7px; }
  .login-screen--small .signup-band { height: 44px; padding-top: 8px; }
  .signup-band__prompt { display: block; }
  .login-screen--large .signup-band__prompt { font-size: 16px; }
  .login-screen--small .signup-band__prompt { font-size: 13px; }
  .signup-band__forgot { display: block; color: var(--link); }
  .login-screen--large .signup-band__forgot { font-size: 10px; margin-top: 3px; }
  .login-screen--small .signup-band__forgot { font-size: 8px; margin-top: 3px; }
</style>
</head>
<body>

  <div class="app-icon app-icon--glossy">
    <div class="app-icon__art" role="img" aria-label="Glossy cloud with a gold padlock"></div>
  </div>
  <div class="app-icon app-icon--flat">
    <div class="app-icon__art" role="img" aria-label="White cloud with a gold padlock"></div>
  </div>

  <section class="login-screen login-screen--large">
    <div class="status-bar">
      <span class="status-bar__carrier">
        <span class="signal"><i style="height:3px"></i><i style="height:4px"></i><i style="height:5px"></i><i style="height:6px"></i><i style="height:7px"></i></span>
        Movinta
      </span>
      <span class="status-bar__time">14:48</span>
      <span class="status-bar__right">18 % <span class="battery"></span></span>
    </div>
    <h1 class="app-title">Nimbo Mobile</h1>
    <div class="login-form">
      <div class="field-group">
        <div class="field">Email</div>
        <div class="field">Password</div>
      </div>
      <div class="login-button">Log In</div>
    </div>
    <div class="signup-band">
      <span class="signup-band__prompt">Not a Member Yet? Sign up.</span>
      <span class="signup-band__forgot">Forgot password?</span>
    </div>
  </section>

  <section class="login-screen login-screen--small">
    <div class="status-bar">
      <span class="status-bar__carrier">
        <span class="signal"><i style="height:2px"></i><i style="height:3px"></i><i style="height:4px"></i><i style="height:5px"></i><i style="height:6px"></i></span>
        Movinta
      </span>
      <span class="status-bar__time">14:48</span>
      <span class="status-bar__right">18 % <span class="battery"></span></span>
    </div>
    <h1 class="app-title">Nimbo Mobile</h1>
    <div class="cloud-art" role="img" aria-label="White cloud rising behind the login form"></div>
    <div class="login-form">
      <div class="field-group">
        <div class="field">Email</div>
        <div class="field">Password</div>
      </div>
      <div class="login-button">Log In</div>
    </div>
    <div class="signup-band">
      <span class="signup-band__prompt">Not a Member Yet? Sign up.</span>
      <span class="signup-band__forgot">Forgot password?</span>
    </div>
  </section>

</body>
</html>
```